Build a fresh, contemporary website for a marriage and funeral celebrant

Hi, I'm a marriage celebrant looking for a great redesign of my website.

The site needs to be bright, friendly and full of love and reflect my personality.
I am earthy, friendly, funky, a bit of a hippy, spiritual, caring, creative, professional. I care about the planet, people and believe that love is the answer.

My main area is weddings, but I also offer funerals. I create meaningful, personal ceremonies for any occasion and present them with warmth, humour and compassion.

My current website is hosted by PLOMA, which I hear is not great with zendor. Initial SEO, white hat and all that jazz must be included with the accepted design.

Please see my current website at www.willowvowrites.com.au
PLEASE DO NOT PHONE. I prefer to communicate through the freelancer portal to keep my email free for client contact.

Copy and images will be uploaded

```html
<!DOCTYPE html>
<html lang="en">
<head>
<meta charset="utf-8">
<title>Mara Linden Celebrant</title>
<link rel="stylesheet" href="https://fonts.googleapis.com/css2?family=Parisienne&family=Poppins:wght@300;400;500&display=swap">
<style>
:root{
  --pink:#d84fd6;
  --pink-soft:#f2b6ee;
  --ink:#222;
  --text:#444;
  --grey-band:#eeeeee;
  --white:#fff;
  --gold:#e3c24a;
  --line:#e6e6e6;
}
*{box-sizing:border-box;margin:0;padding:0}
html,body{width:1200px;height:2252px;overflow:hidden;background:var(--white)}
body{font-family:"Poppins",sans-serif;color:var(--text);position:relative}
.abs{position:absolute}
.script{font-family:"Parisienne",cursive}

/* nav */
.site-nav{top:0;left:0;width:1200px;height:60px;background:var(--white)}
.brand{left:150px;top:12px;font-size:19px;font-weight:500;color:var(--ink);letter-spacing:.5px;line-height:36px;display:flex;align-items:center;gap:8px}
.brand-dot{width:14px;height:14px;border-radius:50%;background:var(--ink)}
.nav-links{right:150px;top:22px;display:flex;gap:34px;list-style:none;font-size:10.5px;font-weight:500;color:var(--ink);letter-spacing:.3px}
.nav-links .active{color:var(--pink)}

/* hero */
.hero{top:60px;left:0;width:1200px;height:427px;background:linear-gradient(180deg,#4c5a3a 0%,#2f3b25 45%,#5d6a48 80%,#8a9270 100%)}
.hero-copy{top:135px;left:0;width:1200px;text-align:center;color:var(--white)}
.hero-name{font-size:34px;line-height:44px}
.hero-role{font-size:44px;color:var(--pink);font-weight:400;line-height:52px;letter-spacing:1px}
.hero-phone{font-family:"Parisienne",cursive;font-size:26px;line-height:44px;letter-spacing:2px;font-style:normal}
.btn{display:inline-block;width:112px;height:34px;line-height:34px;border-radius:17px;background:var(--pink);color:var(--white);font-size:13px;font-weight:500;text-align:center}
.hero .btn{position:absolute;top:304px;left:556px;border:2px solid var(--white);line-height:30px}

/* intro */
.intro{top:540px;left:0;width:1200px;text-align:center}
.intro-hey{font-size:13px;color:var(--ink)}
.intro-title{font-size:24px;color:var(--ink);margin-top:2px}
.intro-text{width:630px;margin:28px auto 0;font-size:11.3px;line-height:22.4px;color:var(--text)}
.intro .btn{margin-top:30px}
.corner{top:730px;width:155px;height:147px;background:radial-gradient(circle at 40% 60%,var(--pink-soft) 0%,#f7d6f4 60%,transparent 75%)}
.corner-left{left:0}
.corner-right{right:0}

/* gallery */
.gallery{top:877px;left:0;width:1200px;height:636px;background:var(--grey-band)}
.section-title{width:1200px;text-align:center;font-size:25px;color:var(--ink);left:0}
.flourish{width:72px;height:16px;left:564px;background:linear-gradient(90deg,transparent,var(--pink) 20%,var(--pink) 80%,transparent);opacity:.7;border-radius:8px}
.grid{top:140px;left:0;width:1200px;display:grid;grid-template-columns:repeat(4,300px);grid-template-rows:repeat(2,228px)}
.tile:nth-child(1){background:linear-gradient(160deg,#6d7f4a,#c9c7bd)}
.tile:nth-child(2){background:linear-gradient(160deg,#dfdde4,#e87a2e 70%,#c9c6d0)}
.tile:nth-child(3){background:linear-gradient(160deg,#6e5a45,#3b3836 70%,#9a8f80)}
.tile:nth-child(4){background:linear-gradient(160deg,#7a9a55,#e8e4dc 60%,#a4a99a)}
.tile:nth-child(5){background:linear-gradient(160deg,#3d4330,#6a6b55 60%,#e0ddd6)}
.tile:nth-child(6){background:linear-gradient(160deg,#eadcd2,#2d3138 65%,#50555c)}
.tile:nth-child(7){background:radial-gradient(circle at 50% 55%,#f07a1c 0%,#e86a15 40%,#ddd8d4 75%)}
.tile:nth-child(8){background:linear-gradient(180deg,#9ea1a5,#575b5f 55%,#3a3c3d)}

/* reviews */
.arrow{top:1612px;width:25px;height:25px;border-radius:50%;background:var(--pink)}
.review-photo{top:1637px;left:150px;width:222px;height:223px;background:linear-gradient(160deg,#7a9a55,#e8e4dc 60%,#a4a99a)}
.review-card{top:1665px;left:335px;width:715px;height:223px;background:var(--white);box-shadow:0 2px 10px rgba(0,0,0,.16);text-align:center;padding:30px 20px 0 40px}
.review-text{font-size:11.3px;line-height:22.4px;color:var(--ink)}
.review-title{margin-top:18px;font-size:16px;font-weight:500;color:var(--ink)}
.review-name{font-size:11px;color:var(--ink);margin-top:4px}
.stars{margin-top:10px;display:flex;justify-content:center;gap:2px}

/* footer */
.footer{top:1945px;left:0;width:1200px;text-align:center;color:var(--ink)}
.footer-brand{font-size:26px;font-weight:500;display:flex;justify-content:center;align-items:center;gap:10px;height:72px}
.footer-brand .brand-dot{width:18px;height:18px}
.footer-contact{margin-top:20px;font-size:11.3px;line-height:22.5px;list-style:none}
.social{margin-top:12px;display:flex;justify-content:center;gap:18px}
.social span{width:8px;height:8px;border-radius:50%;background:var(--ink)}
.footer-rule{top:2188px;left:0;width:1200px;height:1px;background:var(--line)}
.copyright{top:2212px;left:438px;font-size:10px;color:var(--ink)}
.credit{top:2212px;left:621px;font-size:10px;color:var(--pink)}
.badge{top:2195px;left:982px;width:65px;height:50px;border-radius:6px;background:linear-gradient(90deg,#e0433a,#f1b33a 35%,#3fa3d8 70%,#6a55b8)}
</style>
</head>
<body>

<header class="site-nav abs">
  <div class="brand abs"><span class="brand-dot"></span>Willow Vows</div>
  <ul class="nav-links abs">
    <li class="active">HOME</li>
    <li>MEET MARA</li>
    <li>RAVE REVIEWS</li>
    <li>LOVE LOVE LOVE</li>
    <li>SAY HI</li>
    <li>LINKS</li>
  </ul>
</header>

<section class="hero abs" role="img" aria-label="Bride and groom walking hand in hand through a green garden">
  <div class="hero-copy abs">
    <p class="hero-name script">Mara Linden</p>
    <h1 class="hero-role">Celebrant</h1>
    <p class="hero-phone">0400 217 664</p>
  </div>
  <span class="btn">Let it go!</span>
</section>

<div class="corner corner-left abs" role="img" aria-label="Pink floral corner ornament"></div>
<div class="corner corner-right abs" role="img" aria-label="Pink floral corner ornament"></div>

<section class="intro abs">
  <p class="intro-hey script">Hey there,</p>
  <h2 class="intro-title script">I'm Mara,</h2>
  <p class="intro-text">....lover of mountains, chocolate and echidnas. I've been crafting unique ceremonies for amazing people since 2012 and truly love sharing the joy as they mark their most memorable moments in life.I live on 20 acres near Fernvale in Northern Tasmania with my beautiful husband and 3 gloriously happy and cheeky children.I spend my time growing veggies, battling thistles and managing a mini-menagerie, winding down with a glass of great shiraz and a good book.I'm inspired by nature, passion, and those who fearlessly follow their dreams.</p>
  <span class="btn">Let it go!</span>
</section>

<section class="gallery abs">
  <h2 class="section-title script abs" style="top:52px">Love Love Love</h2>
  <div class="flourish abs" style="top:92px" role="img" aria-label="Pink flourish ornament"></div>
  <div class="grid abs">
    <div class="tile" role="img" aria-label="Wedding ceremony in a garden"></div>
    <div class="tile" role="img" aria-label="Jars of wildflowers"></div>
    <div class="tile" role="img" aria-label="Groom having a buttonhole pinned"></div>
    <div class="tile" role="img" aria-label="Couple embracing among trees"></div>
    <div class="tile" role="img" aria-label="Couple standing in a forest with celebrant"></div>
    <div class="tile" role="img" aria-label="Bride leaning on groom's shoulder"></div>
    <div class="tile" role="img" aria-label="Bouquet of orange roses"></div>
    <div class="tile" role="img" aria-label="Couple in front of a mountain"></div>
  </div>
</section>

<h2 class="section-title script abs" style="top:1570px">Rave Reviews</h2>
<div class="flourish abs" style="top:1613px" role="img" aria-label="Pink flourish ornament"></div>

<span class="arrow abs" style="left:991px"><svg width="25" height="25" viewBox="0 0 25 25"><path d="M14 8l-4.5 4.5L14 17" fill="none" stroke="#fff" stroke-width="2"/></svg></span>
<span class="arrow abs" style="left:1024px"><svg width="25" height="25" viewBox="0 0 25 25"><path d="M11 8l4.5 4.5L11 17" fill="none" stroke="#fff" stroke-width="2"/></svg></span>

<div class="review-photo abs" role="img" aria-label="Couple embracing outdoors"></div>
<article class="review-card abs">
  <p class="review-text">We were after a celebrant who was a bit'left of centre', like we are. We met with Mara a liked her immediately. She was warm, friendly, and fun from the outset. Mara helped us every step of the way with herprofessional, but caring,</p>
  <h3 class="review-title">Best Wedding Ever!</h3>
  <p class="review-name">Lorem ipsum</p>
  <div class="stars">
    <svg width="78" height="13" viewBox="0 0 78 13" fill="var(--gold)">
      <path id="st" d="M6.5 0l1.9 4.3 4.6.4-3.5 3 1.1 4.6-4.1-2.5-4.1 2.5 1.1-4.6L0 4.7l4.6-.4z"/>
      <use href="#st" x="16"/><use href="#st" x="32"/><use href="#st" x="48"/><use href="#st" x="64"/>
    </svg>
  </div>
</article>

<footer class="footer abs">
  <div class="footer-brand"><span class="brand-dot"></span>Willow Vows</div>
  <ul class="footer-contact">
    <li>12 Fernbrook Rd, Hollow Creek, Tasmania</li>
    <li>phone: 0400 217 664</li>
    <li>love@willowvowrites.com.au</li>
  </ul>
  <div class="social"><span></span><span></span><span></span><span></span></div>
</footer>

<div class="footer-rule abs"></div>
<p class="copyright abs">Copyright Mara Linden Celebrant</p>
<p class="credit abs">No Animals were harmed in the making.</p>
<div class="badge abs" role="img" aria-label="Professional membership badge"></div>

</body>
</html>
```